Up and Coming Software Company needs a universal, cutting edge power point template.

Looking for a PowerPoint template designed for our company 'Vantor Chart Plus'. We supply dental software to practices across North America. I will attach our corporate logo and you can visit our website @ www.vantorchart.example so you can garner an idea of what kind of look and colors we are going for. A somewhat unique slide master would be appreciated, we like a clean, modern approach to our presentations. Our application is designed to save office staff time, increase revenues and eliminate the loss of patients. We are also the most comprehensive patient recall product in the marketplace today.

Target Market(s)

dentists, partner corporations, office managers - 35-50 yrs old

Industry/Entity Type

Dental

Requirements
Must have
• Our Logo, corporate colors. Must be compatible with all recent versions of PowerPoint
Should not have
• Pictures of teeth, toothbrushes etc. Anything cliche with respect to dentistry.

```html
<!DOCTYPE html>
<html lang="en">
<head>
<meta charset="utf-8">
<title>Vantor Chart Plus – Presentation Template</title>
<link href="https://fonts.googleapis.com/css2?family=Montserrat:wght@400;600;700;800&family=Raleway:wght@300;400;500&display=swap" rel="stylesheet">
<style>
:root{
  --green:#1f8a3c;
  --green-dark:#16702f;
  --ink:#222;
  --body:#7a7a7a;
  --band:#e6e6e4;
  --pill:#c9c9c6;
  --blue:#5a82a6;
  --sky:#6cb4da;
  --olive:#7da64f;
  --lime:#a3bb45;
  --gold:#d3a23f;
  --line-blue:#1a5fae;
  --bar-dark:#b9aea3;
  --bar-light:#eeeae0;
}
*{margin:0;padding:0;box-sizing:border-box}
html,body{width:1067px;height:1200px;overflow:hidden;background:#fff}
.deck{width:1200px;height:1350px;transform:scale(.88917);transform-origin:0 0;position:relative;font-family:"Raleway",sans-serif;color:var(--body)}
.slide{position:absolute;width:600px;height:450px;overflow:hidden;background:linear-gradient(180deg,#f4f4f3 0%,#e9e9e7 100%)}
.s-tl{left:0;top:0}.s-tr{left:600px;top:0}.s-ml{left:0;top:450px}.s-mr{left:600px;top:450px}.s-bl{left:0;top:900px}.s-br{left:600px;top:900px}
.card{position:absolute;left:0;top:15px;width:581px;height:377px;background:radial-gradient(ellipse at 30% 30%,#fff 55%,#f3f3f2 100%)}
.s-tr .card,.s-mr .card,.s-br .card{left:0}
.tab{position:absolute;left:14px;top:0;width:25px;height:40px;background:var(--green);border-radius:0 0 12px 12px;color:#fff;font:700 13px "Montserrat",sans-serif;display:flex;align-items:flex-end;justify-content:center;padding-bottom:6px}
.footer{position:absolute;left:0;top:392px;width:600px;height:58px}
.brand{position:absolute;left:16px;top:16px;display:flex;align-items:center;gap:8px;font:700 16px "Montserrat",sans-serif;color:var(--green)}
.brand .dot{width:28px;height:28px;border-radius:50%;background:var(--green)}
.pill{position:absolute;top:21px;height:15px;border-radius:8px;background:var(--pill);color:#fff;font:400 8px "Montserrat",sans-serif;line-height:15px;text-align:center}
.pill.web{left:315px;width:118px}.pill.tel{left:443px;width:137px}
h1{font:800 22px "Montserrat",sans-serif;color:var(--ink);line-height:1.1}
h2{font:400 22px "Raleway",sans-serif;color:var(--ink)}
p{font-size:12px;line-height:16.5px;text-align:justify}

/* cover */
.s-tl{background:#fff}
.cover-photo{position:absolute;left:290px;top:0;width:310px;height:450px;background:radial-gradient(circle at 160px 190px,#d9a597 0%,#e8c9bd 30%,#f1e4de 55%,#fff 80%)}
.cover-title{position:absolute;left:22px;top:132px;font:300 34px "Raleway",sans-serif;color:#333;line-height:32px}
.cover-meta{position:absolute;left:22px;top:236px;font:500 14px "Raleway",sans-serif;color:var(--green)}
.cover-brand{position:absolute;left:30px;top:365px;display:flex;align-items:center;gap:12px;font:700 22px "Montserrat",sans-serif;color:var(--green)}
.cover-brand .dot{width:50px;height:50px;border-radius:50%;background:var(--green)}

/* slide 04 */
.bubble{position:absolute;border-radius:50%;color:#fff;display:flex;align-items:center;justify-content:center;text-align:center;font:400 11px "Montserrat",sans-serif;line-height:14px;padding:0 14px}
.bubble.small{font-size:9.5px;line-height:12.5px;border-radius:50px;padding:0 18px}

/* slide 02 / 07 photo */
.photo{position:absolute}
/* slide 03 circles */
.feature{position:absolute;top:1085px;width:178px;height:178px;border-radius:50%;color:#fff;text-align:center;font:400 13px "Montserrat",sans-serif;line-height:16px;padding-top:102px}
.feature b{font-weight:700;display:block}
.feature hr{border:0;border-top:1px solid rgba(255,255,255,.8);width:110px;margin:0 auto 10px}
</style>
</head>
<body>
<div class="deck">

  <!-- Cover -->
  <section class="slide s-tl">
    <div class="cover-photo" role="img" aria-label="Photo of a patient in a dental chair with soft coloured light strokes"></div>
    <div class="cover-title">Patient recall<br>has never<br>been easier</div>
    <div class="cover-meta">Jane Ellis,&nbsp; 01 Feb 2014</div>
    <div class="cover-brand"><span class="dot"></span>Vantor Chart Plus</div>
  </section>

  <!-- 04 -->
  <section class="slide s-tr">
    <div class="card">
      <div class="tab">04</div>
      <h1 style="position:absolute;left:49px;top:20px">Lorem Ipsum is simply dummy text of<br>the printing and typesetting industry.</h1>
      <p style="position:absolute;left:49px;top:80px;width:510px;text-align:left">Lorem Ipsum has been the industry's standard dummy text ever since the 1500s, when an unknown printer took but also the leap into electronic typesetting, remaining essentially unchanged.</p>
      <svg width="581" height="377" style="position:absolute;left:0;top:0" fill="none" stroke="#555" stroke-dasharray="3 3">
        <path d="M137 252H165V195H195M165 252V305H195"/>
        <path d="M392 195H420V305H392M420 252H446"/>
      </svg>
      <div class="bubble" style="left:28px;top:197px;width:108px;height:108px;background:var(--blue)">Lorem Ipsum is simply dummy</div>
      <div class="bubble small" style="left:194px;top:142px;width:198px;height:100px;background:var(--olive)">Contrary to popular belief, Lorem Ipsum is not simply random text. It has roots in a piece of classical Latin literature from 45 BC, making it over 2000</div>
      <div class="bubble small" style="left:194px;top:253px;width:198px;height:100px;background:var(--sky)">There are many variations of passages of Lorem Ipsum available, but the majority have suffered alteration in some form, by injected humour.</div>
      <div class="bubble" style="left:446px;top:197px;width:108px;height:108px;background:var(--lime)">Lorem Ipsum is simply dummy</div>
    </div>
    <div class="footer"><div class="brand"><span class="dot"></span>Vantor Chart Plus</div><div class="pill web">www.vantorchart.example</div><div class="pill tel">Call Toll Free&nbsp;&nbsp; 1-800-555-0142</div></div>
  </section>

  <!-- 02 -->
  <section class="slide s-ml">
    <div class="card">
      <div class="tab">02</div>
      <h1 style="position:absolute;left:49px;top:16px">Intelligent Design</h1>
      <h2 style="position:absolute;left:49px;top:40px">Automation meets organization</h2>
      <div class="photo" role="img" aria-label="Photo of a smiling office manager at a computer screen" style="left:0;top:103px;width:245px;height:188px;border-radius:0 95px 95px 0;background:linear-gradient(90deg,#6d7a7d 0%,#a9b0ad 40%,#e0c9b0 70%,#c9d4d8 100%)"></div>
      <p style="position:absolute;left:270px;top:108px;width:283px">You run a busy practice. What you don't need is software that keeps you guessing, software that slows you down and complicates your workday.</p>
      <p style="position:absolute;left:270px;top:190px;width:283px">Vantor Chart Plus sits on your desktop right next to your scheduler which is where it should be, organizing time consuming tasks so you don't have to. Let us reduce your workloads, streamline your day and enhance your schedule – all at the same time.</p>
    </div>
    <div class="footer"><div class="brand"><span class="dot"></span>Vantor Chart Plus</div><div class="pill web">www.vantorchart.example</div><div class="pill tel">Call Toll Free&nbsp;&nbsp; 1-800-555-0142</div></div>
  </section>

  <!-- 07 -->
  <section class="slide s-mr">
    <div class="card">
      <div class="tab">07</div>
      <h1 style="position:absolute;left:49px;top:16px">Lorem Ipsum</h1>
      <h2 style="position:absolute;left:49px;top:40px">There are many variations</h2>
      <p style="position:absolute;left:49px;top:83px;width:283px">It is a long established fact that a reader will be distracted by the readable content of a page when looking at its layout. The point of using Lorem Ipsum is that it has a more-or-less normal distribution of letters, as opposed to using 'Content here, content here', making it look like readable English.</p>
      <p style="position:absolute;left:49px;top:215px;width:283px">Many desktop publishing packages and web page editors now use Lorem Ipsum as their default model text, and a search for 'lorem ipsum' will uncover many web sites still in their infancy. Various versions have evolved over the years, sometimes by accident, sometimes on purpose (injected humour and the like).</p>
      <div class="photo" role="img" aria-label="Photo of a dentist in a blue shirt and face mask holding instruments" style="left:407px;top:50px;width:174px;height:310px;border-radius:90px 0 0 90px;background:linear-gradient(160deg,#e8eef2 0%,#c9a68c 30%,#2f7fc8 60%,#1f5fa3 100%)"></div>
    </div>
    <div class="footer"><div class="brand"><span class="dot"></span>Vantor Chart Plus</div><div class="pill web">www.vantorchart.example</div><div class="pill tel">Call Toll Free&nbsp;&nbsp; 1-800-555-0142</div></div>
  </section>

  <!-- 03 -->
  <section class="slide s-bl">
    <div class="card">
      <div class="tab">03</div>
      <h1 style="position:absolute;left:49px;top:14px;font-size:26px">Designed with your practice in mind</h1>
      <p style="position:absolute;left:49px;top:67px;width:476px;font-size:13px;line-height:16.5px">Vantor Chart Plus has been put to the test in the most demanding dental offices.&nbsp; The end result?&nbsp; The most advanced and intuitive patient recall solution available today.</p>
      <p style="position:absolute;left:49px;top:125px;width:480px;font-size:13px;text-align:left">Grow your practice – enhance your daily workflow - get more done in less time</p>
    </div>
    <div class="feature" style="left:49px;top:185px;background:var(--sky);mix-blend-mode:multiply">
      <svg width="100" height="30" viewBox="0 0 100 30" style="position:absolute;left:39px;top:42px" fill="#fff"><path d="M4 8l8-5 8 5v10l-8 5-8-5z"/><rect x="23" y="9" width="10" height="8" rx="2"/><rect x="39" y="10" width="12" height="6"/><path d="M62 8l8-5 8 5v10l-8 5-8-5z"/><circle cx="70" cy="13" r="4" fill="var(--sky)"/></svg>
      <hr><b>Seamless Integration</b>Information when<br>you need it
    </div>
    <div class="feature" style="left:200px;top:185px;background:var(--gold);mix-blend-mode:multiply">
      <svg width="90" height="56" viewBox="0 0 90 56" style="position:absolute;left:44px;top:24px" fill="#fff"><circle cx="32" cy="14" r="12"/><path d="M6 54c0-18 10-26 26-26s26 8 26 26z"/><circle cx="62" cy="20" r="10"/><path d="M60 54c0-8-2-14-6-19 3-2 6-3 9-3 14 0 21 7 21 22z"/></svg>
      <hr><b>Multiple Users</b>Work as a team
    </div>
    <div class="feature" style="left:350px;top:185px;background:var(--lime);mix-blend-mode:multiply">
      <svg width="60" height="60" viewBox="0 0 60 60" style="position:absolute;left:59px;top:24px" fill="none" stroke="#fff" stroke-width="3"><circle cx="30" cy="30" r="16"/><path d="M30 6v8M30 46v8M6 30h8M46 30h8M13 13l6 6M41 41l6 6M47 13l-6 6M13 47l6-6"/><path d="M23 34v-8l7-5 7 5v8z" fill="#fff"/></svg>
      <hr><b>Multiple Practices</b>Infinite possibilities
    </div>
    <div class="footer"><div class="brand"><span class="dot"></span>Vantor Chart Plus</div><div class="pill web">www.vantorchart.example</div><div class="pill tel">Call Toll Free&nbsp;&nbsp; 1-800-555-0142</div></div>
  </section>

  <!-- 06 -->
  <section class="slide s-br">
    <div class="card">
      <div class="tab">06</div>
      <h1 style="position:absolute;left:49px;top:14px;font-size:34px">Lorem Ipsum</h1>
      <p style="position:absolute;left:49px;top:77px;width:480px;font-size:12.5px;text-align:left">It is a long established fact that a reader will be distracted by the readable content of a page when looking at its layout. The point of using Lorem Ipsum is that</p>
    </div>
    <svg class="chart" width="600" height="392" style="position:absolute;left:0;top:0" font-family="Montserrat, sans-serif">
      <polygon points="65,149 138,230 138,350 65,350" fill="var(--bar-dark)"/>
      <polygon points="138,230 212,251 212,350 138,350" fill="var(--bar-light)"/>
      <polygon points="212,251 284,255 284,350 212,350" fill="var(--bar-dark)"/>
      <polygon points="284,255 358,311 358,350 284,350" fill="var(--bar-light)"/>
      <polygon points="358,311 443,311 443,350 358,350" fill="var(--bar-dark)"/>
      <polygon points="443,311 517,324 517,350 443,350" fill="var(--bar-light)"/>
      <polyline points="65,149 138,230 212,251 284,255 358,311 443,311 517,324" fill="none" stroke="var(--line-blue)" stroke-width="3"/>
      <g fill="var(--green)" stroke="#8ed09a" stroke-width="2">
        <circle cx="65" cy="149" r="8"/><circle cx="138" cy="230" r="8"/><circle cx="212" cy="251" r="8"/><circle cx="284" cy="255" r="8"/><circle cx="358" cy="311" r="8"/><circle cx="443" cy="311" r="8"/><circle cx="517" cy="324" r="8"/>
      </g>
      <g font-size="8" fill="#555">
        <text x="79" y="152">0.733</text><text x="149" y="218">0.658</text><text x="222" y="239">0.638</text><text x="294" y="244">0.634</text><text x="367" y="298">0.581</text><text x="451" y="298">0.580</text><text x="520" y="310">0.568</text>
      </g>
      <g font-size="8.5" fill="#777" text-anchor="middle">
        <text x="82" y="365">January</text><text x="146" y="365">February</text><text x="215" y="365">March</text><text x="283" y="365">April</text><text x="357" y="365">May</text><text x="442" y="365">June</text><text x="505" y="365">July</text>
      </g>
      <path d="M288 164h8v-8h8v8h8l-12 12z" fill="var(--line-blue)"/>
      <text x="306" y="186" font-size="28" font-weight="700" fill="var(--line-blue)">22.5%</text>
    </svg>
    <div class="footer"><div class="brand"><span class="dot"></span>Vantor Chart Plus</div><div class="pill web">www.vantorchart.example</div><div class="pill tel">Call Toll Free&nbsp;&nbsp; 1-800-555-0142</div></div>
  </section>

</div>
</body>
</html>
```